Private Gym Needs a Rack Card Design

We need a basic front and back rack card (same size as post card) that gives basic information about our brand, and includes our logo. Please see attached logo and required content below.

Target Market(s)

Upscale, private gym.

Industry/Entity Type

Gym

Font styles to use
Sans Serif

Colors
ffffff
5c5c5c
000000
dbdbdb
f78f20

Requirements
Must have
• Business Logo and the following text in a clean, modern, easy-to-read, artistic manner. Style and design must be clean, incorporate our color scheme of MOSTLY white, light grey, charcoal, with just pops of orange. We want the card itself to be mostly white background. Must include website URL as well: corevaultfitness.com
• FRONT CARD:
• Logo
• A safe and individualized approach to exercise
• our path employs the latest weight resistance training exercises and coaching for healthy living. Not only is our workout methodology effective, it’s safe.
• Our Path…
• -Improves Functional Movement
• -Promotes Weight Loss
• -Builds Strength
• -Increases Flexibility 

• BACK:
• Change Your Body. Find Your Strength.
• There’s 40 years of success behind our proven method
• What is Iron Path? 
• Iron Path is all about teaching our clients how to lift weights and exercise with the proper technique. There’s no slinging or jerking at our gym; only controlled movements that yield real results.
• Come workout with us in our private gym. We are located in Durham adjacent to Larch Campus and 5 minutes from downtown Durham.
• Address: 482 Fenwick Ave, Durham, NC 27705
• Phone: (919) 555-0147
• Hours: 9:00 AM – 9:00 PM
Nice to have
• Great organization of text, maybe some columns, colored bullet points, cool graphics and logos.
Should not have
• Busy or crowded design. All lines should be sleek, straight, and streamline. NO STOCK IMAGES, but logos are GREAT

```html
<!DOCTYPE html>
<html lang="en">
<head>
<meta charset="utf-8">
<title>Iron Path – Rack Card</title>
<link rel="stylesheet" href="https://fonts.googleapis.com/css2?family=Roboto+Condensed:wght@400;500;700&family=Roboto:wght@400;500&display=swap">
<style>
  :root {
    --backdrop: #a7a8ab;
    --paper: #ffffff;
    --charcoal: #58585a;
    --mid-grey: #8a8a8c;
    --light-grey: #b5b5b7;
    --ink: #3a3a3c;
    --orange: #ef4a24;
    --perforation: #7fc4e0;
  }
  * { margin: 0; padding: 0; box-sizing: border-box; }
  html, body { width: 1200px; height: 1040px; overflow: hidden; background: var(--backdrop); }
  body { position: relative; font-family: "Roboto Condensed", "Arial Narrow", sans-serif; color: var(--charcoal); }

  .card {
    position: absolute; left: 29px; width: 1142px; height: 470px;
    background: var(--paper);
    box-shadow: 5px 5px 4px rgba(0,0,0,0.35);
    overflow: hidden;
  }
  .card--front { top: 29px; }
  .card--back { top: 544px; }
  .abs { position: absolute; white-space: nowrap; }

  .perforation {
    position: absolute; left: 877px; top: 0; bottom: 0;
    border-left: 1px dashed var(--perforation);
  }
  .stub { position: absolute; left: 878px; top: 0; width: 264px; height: 470px; }

  /* Front */
  .brand-name {
    left: 67px; top: 78px; font-size: 100px; font-weight: 700; line-height: 1;
    color: var(--charcoal); letter-spacing: 1px; display: flex; align-items: center; gap: 18px;
  }
  .brand-name .brand-square { width: 28px; height: 28px; background: var(--orange); display: inline-block; }

  .tagline-band { left: 0; top: 244px; width: 602px; height: 43px; background: var(--charcoal); }
  .tagline-band span {
    position: absolute; left: 67px; top: 9px; color: #fff;
    font-family: "Roboto", Arial, sans-serif; font-size: 21px;
  }
  .band-end { left: 821px; top: 244px; width: 57px; height: 43px; background: var(--charcoal); }
  .band-stripes { left: 610px; top: 244px; }

  .statement { left: 610px; top: 64px; width: 202px; text-transform: uppercase; line-height: 1; }
  .statement p { white-space: nowrap; }
  .statement .s-lead { font-size: 21px; font-weight: 500; color: var(--ink); }
  .statement .s-small { font-size: 10.5px; font-weight: 500; color: var(--ink); margin-top: 3px; }
  .statement .s-light { font-size: 18.5px; color: var(--mid-grey); margin-top: 2px; }
  .statement .s-bold { font-size: 22px; font-weight: 500; color: var(--ink); margin-top: 2px; }
  .statement .s-large-light { font-size: 28px; color: var(--mid-grey); margin-top: 1px; }
  .statement .s-huge { font-size: 49px; font-weight: 700; color: var(--charcoal); margin-top: 2px; }

  .benefits-title { left: 67px; top: 305px; font-size: 33px; font-weight: 500; color: var(--orange); }
  .benefit-list { list-style: none; font-family: "Roboto", Arial, sans-serif; font-size: 26px; color: var(--orange); line-height: 32px; }
  .benefit-list li { display: flex; align-items: center; gap: 16px; white-space: nowrap; }
  .benefit-list li::before { content: ""; width: 12px; height: 12px; background: var(--orange); flex: none; }
  .benefits-left { left: 67px; top: 346px; }
  .benefits-right { left: 567px; top: 346px; }

  /* Back */
  .headline { left: 67px; top: 60px; line-height: 1; text-transform: uppercase; }
  .headline .h-dark { font-size: 29px; font-weight: 500; color: var(--charcoal); }
  .headline .h-grey { font-size: 29px; font-weight: 500; color: var(--mid-grey); margin-top: 2px; }
  .headline .h-small { font-size: 14px; color: var(--mid-grey); margin-top: 4px; }
  .headline .h-dark-2 { font-size: 29px; font-weight: 500; color: var(--charcoal); margin-top: 3px; }

  .website { right: 331px; top: 100px; font-size: 25px; color: var(--ink); }

  .about-band { left: 0; top: 189px; width: 877px; height: 127px; background: var(--orange); color: #fff; }
  .about-band h2 { position: absolute; left: 67px; top: 20px; font-size: 34px; font-weight: 700; white-space: nowrap; }
  .about-band p { position: absolute; left: 67px; top: 64px; font-size: 18px; line-height: 22px; white-space: nowrap; }

  .location { left: 67px; top: 343px; line-height: 1; text-transform: uppercase; }
  .location .l-small { font-size: 11.5px; color: var(--ink); }
  .location .l-mid { font-size: 19px; color: var(--charcoal); margin-top: 2px; }
  .location .l-light { font-size: 19px; color: var(--mid-grey); margin-top: 1px; }
  .location .l-small-2 { font-size: 11.5px; color: var(--ink); margin-top: 2px; }

  .contact-row { right: 331px; top: 387px; display: flex; gap: 14px; font-size: 12.5px; color: var(--orange); }
</style>
</head>
<body>

  <section class="card card--front" aria-label="Front of rack card">
    <div class="abs brand-name"><span class="brand-square"></span>IRON PATH</div>

    <div class="abs statement">
      <p class="s-lead">Our Path employs</p>
      <p class="s-small">The latest weight resistance training</p>
      <p class="s-light">Exercises and coaching</p>
      <p class="s-bold">For healthy living.</p>
      <p class="s-large-light">Not only is our</p>
      <p class="s-small">Workout methodology effective,</p>
      <p class="s-huge">It’s safe.</p>
    </div>

    <div class="abs tagline-band"><span>A safe and individualized approach to exercise</span></div>
    <svg class="abs band-stripes" width="202" height="43" viewBox="0 0 202 43" aria-hidden="true">
      <rect x="0" width="7" height="43" fill="#6a6a6c"/>
      <rect x="17" width="7" height="43" fill="#747476"/>
      <rect x="34" width="7" height="43" fill="#808082"/>
      <rect x="51" width="7" height="43" fill="#8e8e90"/>
      <rect x="68" width="7" height="43" fill="#9c9c9e"/>
      <rect x="85" width="7" height="43" fill="#aaaaac"/>
      <rect x="102" width="7" height="43" fill="#b7b7b9"/>
      <rect x="119" width="7" height="43" fill="#aaaaac"/>
      <rect x="136" width="7" height="43" fill="#9c9c9e"/>
      <rect x="153" width="7" height="43" fill="#8e8e90"/>
      <rect x="170" width="7" height="43" fill="#7a7a7c"/>
      <rect x="187" width="7" height="43" fill="#68686a"/>
    </svg>
    <div class="abs band-end"></div>

    <h2 class="abs benefits-title">OUR PATH</h2>
    <ul class="abs benefit-list benefits-left">
      <li>Improves Functional Movement</li>
      <li>Promotes Weight Loss</li>
    </ul>
    <ul class="abs benefit-list benefits-right">
      <li>Builds Strenght</li>
      <li>Increases Flexibility</li>
    </ul>

    <div class="perforation"></div>

    <svg class="stub" viewBox="0 0 264 470" aria-label="Contact reply slip">
      <rect x="39" y="0" width="24" height="470" fill="var(--orange)"/>
      <rect x="39" y="55" width="24" height="112" fill="#f7a68f" opacity="0.55"/>
      <g fill="#ffffff">
        <rect x="39" y="57" width="24" height="3"/><rect x="39" y="64" width="24" height="3"/>
        <rect x="39" y="71" width="24" height="3"/><rect x="39" y="78" width="24" height="3"/>
        <rect x="39" y="85" width="24" height="3"/><rect x="39" y="92" width="24" height="3"/>
        <rect x="39" y="99" width="24" height="3"/><rect x="39" y="106" width="24" height="3"/>
        <rect x="39" y="113" width="24" height="3"/><rect x="39" y="120" width="24" height="3"/>
        <rect x="39" y="127" width="24" height="3"/><rect x="39" y="134" width="24" height="3"/>
        <rect x="39" y="141" width="24" height="3"/><rect x="39" y="148" width="24" height="3"/>
        <rect x="39" y="155" width="24" height="3"/><rect x="39" y="162" width="24" height="3"/>
      </g>
      <g font-family="Roboto Condensed, Arial Narrow, sans-serif" fill="var(--orange)">
        <text transform="translate(93 427) rotate(-90)" font-size="16">INTERESTED IN OUR PATH?</text>
        <text transform="translate(113 427) rotate(-90)" font-size="16">Leave your contact details and we will get back to you.</text>
      </g>
      <g font-family="Roboto, Arial, sans-serif" font-size="11.5" fill="var(--ink)">
        <text transform="translate(156 427) rotate(-90)">Name</text>
        <text transform="translate(186 427) rotate(-90)">Phone</text>
        <text transform="translate(216 427) rotate(-90)">E-mail</text>
      </g>
      <g stroke="#9a9a9c" stroke-width="1" stroke-dasharray="1 2">
        <line x1="151" y1="43" x2="151" y2="371"/>
        <line x1="181" y1="43" x2="181" y2="371"/>
        <line x1="211" y1="43" x2="211" y2="371"/>
      </g>
    </svg>
  </section>

  <section class="card card--back" aria-label="Back of rack card">
    <div class="abs headline">
      <p class="h-dark">Change your body.</p>
      <p class="h-grey">Find your strength.</p>
      <p class="h-small">There’s 40 years of success behind</p>
      <p class="h-dark-2">Our proven method</p>
    </div>

    <p class="abs website">corevaultfitness.com</p>

    <div class="abs about-band">
      <h2>WHAT IS IRON PATH?</h2>
      <p>Iron Path is all about teaching our clients how to lift weights and exercise with the proper technique.<br>There’s no slinging or jerking at our gym; only controlled movements that yield results.</p>
    </div>

    <div class="abs location">
      <p class="l-small">Come workout with us in our private gym.</p>
      <p class="l-mid">We are located in Durham</p>
      <p class="l-light">Adjacent to Larch Campus</p>
      <p class="l-small-2">And 5 minutes from downtown Durham.</p>
    </div>

    <div class="abs contact-row">
      <span>482 Fenwick Ave, Durham, NC 27705</span>
      <span>Phone: (919) 555-0147</span>
      <span>Hours: 9:00 AM – 9:00 PM</span>
    </div>

    <div class="perforation"></div>

    <svg class="stub" viewBox="0 0 264 470" aria-label="Brand stub">
      <rect x="39" y="0" width="24" height="470" fill="var(--charcoal)"/>
      <rect x="39" y="55" width="24" height="112" fill="#ffffff"/>
      <g fill="#8a8a8c">
        <rect x="39" y="57" width="24" height="3"/><rect x="39" y="64" width="24" height="3"/>
        <rect x="39" y="71" width="24" height="3"/><rect x="39" y="78" width="24" height="3"/>
        <rect x="39" y="85" width="24" height="3"/><rect x="39" y="92" width="24" height="3"/>
        <rect x="39" y="99" width="24" height="3"/><rect x="39" y="106" width="24" height="3"/>
        <rect x="39" y="113" width="24" height="3"/><rect x="39" y="120" width="24" height="3"/>
        <rect x="39" y="127" width="24" height="3"/><rect x="39" y="134" width="24" height="3"/>
        <rect x="39" y="141" width="24" height="3"/><rect x="39" y="148" width="24" height="3"/>
        <rect x="39" y="155" width="24" height="3"/><rect x="39" y="162" width="24" height="3"/>
      </g>
      <text transform="translate(170 380) rotate(-90)" font-family="Roboto Condensed, Arial Narrow, sans-serif" font-weight="700" font-size="64" fill="var(--charcoal)">IRON PATH</text>
      <rect x="128" y="392" width="22" height="22" fill="var(--orange)"/>
    </svg>
  </section>

</body>
</html>
```